Business cards for Wine company
Caspellini
Project: Business cards for Wine company
Business cards for Wine company - Beverages
Creative Brief
Simple
Taco Vermeulen
Managing Director
Lindeboomlaan 23 6191KM BEEKDAL
info@caspellini.example
www.caspellini.example
Would be nice if there is a facebook and a twitter in there... @caspellini /caspellini
Be creative!

```html
<!DOCTYPE html>
<html lang="en">
<head>
<meta charset="utf-8">
<title>Caspellini – Business Cards</title>
<link rel="stylesheet" href="https://fonts.googleapis.com/css2?family=Cinzel:wght@400;500;600&display=swap">
<style>
  :root {
    --backdrop: #e8e2d8;
    --paper: #ffffff;
    --ink: #141414;
    --wine: #7d1416;
    --band: #2a2727;
    --band-text: #e9e6e3;
    --muted: #6b6b6b;
    --social-a: #4fb0d8;
    --social-b: #4a6fb0;
  }
  * { margin: 0; padding: 0; box-sizing: border-box; }
  html, body { width: 1200px; height: 978px; overflow: hidden; }
  body {
    background: var(--backdrop);
    position: relative;
    font-family: "Cinzel", serif;
  }
  .card {
    position: absolute;
    box-shadow: 0 3px 10px rgba(0,0,0,.18);
    overflow: hidden;
  }
  /* Front cards with brand name */
  .card--front {
    width: 513px;
    height: 290px;
    display: flex;
    flex-direction: column;
    align-items: center;
    justify-content: center;
    padding-top: 8px;
  }
  .card--black { left: 82px;  top: 365px; background: var(--ink); color: #fff; }
  .card--wine  { left: 616px; top: 365px; background: var(--wine); color: #fff; }
  .card--white { left: 344px; top: 671px; background: var(--paper); color: var(--ink); }

  .brand-name {
    font-size: 50px;
    font-weight: 400;
    letter-spacing: 3px;
    line-height: 1;
  }
  .brand-dot {
    width: 24px; height: 24px;
    border-radius: 50%;
    background: var(--wine);
    margin: 22px 0 22px;
  }
  .card--wine .brand-dot { background: #fff; }
  .est {
    font-size: 16px;
    letter-spacing: 1.5px;
  }

  /* Contact card */
  .card--contact {
    left: 344px; top: 26px;
    width: 515px; height: 286px;
    background: var(--paper);
  }
  .contact-brand {
    position: absolute;
    left: 330px; top: 20px;
    width: 160px;
    display: flex; flex-direction: column; align-items: center; gap: 8px;
    color: var(--wine);
    font-size: 18px;
    letter-spacing: 1.5px;
  }
  .contact-brand .brand-dot { width: 18px; height: 18px; margin: 0; }
  .person {
    position: absolute;
    left: 18px; top: 98px;
  }
  .person-name {
    color: var(--wine);
    font-size: 24px;
    font-weight: 500;
    line-height: 1.1;
  }
  .person-role {
    color: var(--muted);
    font-size: 13px;
    letter-spacing: .5px;
  }
  .contact-band {
    position: absolute;
    left: 13px; top: 164px;
    width: 436px; height: 106px;
    background: var(--band);
    color: var(--band-text);
    display: grid;
    grid-template-columns: 1.2fr 1fr;
    padding: 12px 14px;
    font-size: 11px;
    letter-spacing: .3px;
  }
  .contact-col { display: flex; flex-direction: column; justify-content: space-between; }
  .contact-item { display: flex; align-items: flex-start; gap: 8px; line-height: 1.25; }
  .contact-item svg { flex: none; width: 13px; height: 13px; margin-top: 1px; }
  .social-mark { flex: none; width: 12px; height: 12px; background: var(--social-b); margin-top: 1px; }
  .social-mark--round { border-radius: 50%; background: var(--social-a); }
  .wine-strip {
    position: absolute;
    left: 465px; top: 164px;
    width: 42px; height: 122px;
    background: var(--wine);
  }
</style>
</head>
<body>

  <section class="card card--contact">
    <div class="contact-brand"><span>CASPELLINI</span><span class="brand-dot"></span></div>
    <div class="person">
      <p class="person-name">Taco Vermeulen</p>
      <p class="person-role">Managing Director</p>
    </div>
    <div class="contact-band">
      <div class="contact-col">
        <div class="contact-item">
          <svg viewBox="0 0 12 12"><path d="M6 0.5a4 4 0 0 1 4 4c0 3-4 7-4 7s-4-4-4-7a4 4 0 0 1 4-4z" fill="#e9e6e3"/><circle cx="6" cy="4.5" r="1.5" fill="#2a2727"/></svg>
          <span>: Lindeboomlaan 23<br>6191KM BEEKDAL</span>
        </div>
        <div class="contact-item">
          <svg viewBox="0 0 12 12"><rect x="3" y="0.5" width="6" height="11" rx="1.2" fill="#e9e6e3"/><rect x="4" y="2" width="4" height="6.5" fill="#2a2727"/></svg>
          <span>: +31 612 345 678</span>
        </div>
        <div class="contact-item">
          <svg viewBox="0 0 12 12"><rect x="0.5" y="2.5" width="11" height="7" fill="#e9e6e3"/><path d="M0.5 2.5 6 7l5.5-4.5" fill="none" stroke="#2a2727" stroke-width="1"/></svg>
          <span>: info@caspellini.example</span>
        </div>
      </div>
      <div class="contact-col">
        <div class="contact-item">
          <svg viewBox="0 0 12 12"><circle cx="6" cy="6" r="5" fill="none" stroke="#e9e6e3" stroke-width="1.2"/><path d="M1 6h10M6 1c-2.5 3-2.5 7 0 10M6 1c2.5 3 2.5 7 0 10" fill="none" stroke="#e9e6e3" stroke-width=".9"/></svg>
          <span>: www.caspellini.example</span>
        </div>
        <div class="contact-item">
          <span class="social-mark social-mark--round"></span>
          <span>: @caspellini</span>
        </div>
        <div class="contact-item">
          <span class="social-mark"></span>
          <span>: /caspellini</span>
        </div>
      </div>
    </div>
    <div class="wine-strip"></div>
  </section>

  <section class="card card--front card--black">
    <p class="brand-name">CASPELLINI</p>
    <span class="brand-dot"></span>
    <p class="est">EST 2012</p>
  </section>

  <section class="card card--front card--wine">
    <p class="brand-name">CASPELLINI</p>
    <span class="brand-dot"></span>
    <p class="est">EST 2012</p>
  </section>

  <section class="card card--front card--white">
    <p class="brand-name">CASPELLINI</p>
    <span class="brand-dot"></span>
    <p class="est">EST 2012</p>
  </section>

</body>
</html>
```